The Gemstone Craft Studio Sales Business Card

The goal of this project is to create a interactive & effective business card design for SALES purposes with the intention to get customer on to our website and make a purchase or contact us about a product or service.
Website: WWW.RINGFORGEHUB.COM
GoogleMyBusiness: https://g.page/RingForgeHUB?gm
Facebook & Instagram: @THEGEMSTONECRAFTSTUDIO
Phone # & Text Message & Whatsapp Message: +1(555) 418-0293
Email: HELLO@RINGFORGEHUB.COM
Location: 4872 Brambleton Avenue Suite 512 Larkfield, OR
(It would be necessary to have the appropriate ticker/icon for each social media platform as well as the location ticker and phone / messaging icons instead of spelling the words out.)
It is important to have the company logo and details but with an emphasis toward website. Feel free to also completely make one design your way and completely custom as you feel best.
The Gemstone Craft Studio is a Provider of Luxury Goods & Services such as: Custom Jewelry Design, Jewelry Repairs & Cleaning, Designer Jewelry, Luxury Gifts, 24 Karat Gold, 22 Karat Gold Jewelry, Diamond Jewelry, Insured Jewelry Appraisals, Loose Gemstones & Diamonds, Supporting Sustainability
Target Market(s)
People looking to invest in precious metals and gemstones as well as people looking to find a gift for a loved one for a special occasion. Customers looking to Custom Design Jewelry.
Contact Information for Business Card
Font styles to use
Other font styles liked:
- w.e you want
Colors
Designer to choose colors to be used in the design.
Requirements
Must have
- Website: WWW.RINGFORGEHUB.COM
- GoogleMyBusiness: https://g.page/RingForgeHUB?gm
- Facebook & Instagram: @THEGEMSTONECRAFTSTUDIO
- Phone # & Text Message & Whatsapp Message: +1(555) 418-0293
- Email: HELLO@RINGFORGEHUB.COM
- Location: 4872 Brambleton Avenue Suite 512 Larkfield, OR
- (It would be necessary to have the appropriate ticker/icon for each social media platform as well as the location ticker and phone / messaging icons instead of spelling the words out.)
- It is important to have the company logo and details but with an emphasis toward website. Feel free to also completely make one design your way and completely custom as you feel best.
Nice to have
- The Gemstone Craft Studio is a Provider of Luxury Goods & Services such as: Custom Jewelry Design, Jewelry Repairs & Cleaning, Designer Jewelry, Luxury Gifts, 24 Karat Gold, 22 Karat Gold Jewelry, Diamond Jewelry, Insured Jewelry Appraisals, Loose Gemstones & Diamonds, Supporting Sustainability

```html
<!DOCTYPE html>
<html lang="en">
<head>
<meta charset="utf-8">
<title>The Gemstone Craft Studio – Business Card</title>
<link rel="stylesheet" href="https://fonts.googleapis.com/css2?family=Cinzel:wght@600&family=Arimo:wght@400;700&display=swap">
<style>
  :root {
    --stage: #e9e6e2;
    --card-black: #0b0b0b;
    --brand-red: #e4212f;
    --brand-gold: #f7c93d;
    --text-white: #f2f2f2;
    --text-grey: #a9a9a9;
  }
  * { box-sizing: border-box; margin: 0; padding: 0; }
  html, body {
    width: 1200px; height: 716px; overflow: hidden;
    background: var(--stage);
  }
  .stage {
    position: relative; width: 1200px; height: 716px;
    display: flex; align-items: center; justify-content: center; gap: 40px;
  }
  .card {
    position: relative; width: 540px; height: 309px;
    background: var(--card-black); overflow: hidden;
    box-shadow: 0 6px 18px rgba(0,0,0,.25);
  }
  .brand-name {
    font-family: "Cinzel", serif; font-weight: 600;
    color: var(--brand-red); letter-spacing: .06em; line-height: 1.1;
  }
  .card-front { display: flex; align-items: center; justify-content: center; }
  .card-front .brand-lockup { display: flex; align-items: center; gap: 12px; }
  .brand-mark-dot {
    width: 16px; height: 16px; border-radius: 50%; background: var(--brand-gold);
  }
  .card-front .brand-name { font-size: 26px; text-align: center; }

  .card-back .accent-band {
    position: absolute; top: 0; right: 0; width: 170px; height: 100%;
    background: var(--brand-red);
  }
  .card-back .accent-dot {
    position: absolute; right: 55px; bottom: 60px;
    width: 60px; height: 60px; border-radius: 50%; background: var(--brand-gold);
  }
  .back-content {
    position: absolute; left: 34px; top: 30px; right: 190px;
    font-family: "Arimo", sans-serif;
  }
  .back-content .brand-name { font-size: 20px; margin-bottom: 16px; }
  .person-name { color: var(--brand-gold); font-weight: 700; font-size: 17px; }
  .person-role { color: var(--text-grey); font-size: 10px; margin: 2px 0 12px; }
  .contact-list { list-style: none; }
  .contact-list li {
    display: flex; align-items: center; gap: 7px;
    color: var(--text-white); font-size: 11.5px; line-height: 17px;
    white-space: nowrap;
  }
  .contact-icon { width: 11px; height: 11px; flex: none; fill: var(--brand-gold); }
  .social-pair { display: flex; gap: 2px; }
  .social-square { width: 9px; height: 9px; background: var(--brand-gold); }
  .address { color: var(--text-white); font-size: 11.5px; line-height: 16px; margin-top: 4px; }
</style>
</head>
<body>
<main class="stage">
  <section class="card card-front" aria-label="Card front">
    <div class="brand-lockup">
      <span class="brand-mark-dot"></span>
      <p class="brand-name">The Gemstone<br>Craft Studio</p>
    </div>
  </section>

  <section class="card card-back" aria-label="Card back">
    <div class="accent-band"></div>
    <div class="accent-dot"></div>
    <div class="back-content">
      <p class="brand-name">The Gemstone Craft Studio</p>
      <p class="person-name">Marcus Hale</p>
      <p class="person-role">Manager</p>
      <ul class="contact-list">
        <li>
          <svg class="contact-icon" viewBox="0 0 24 24"><path d="M6.6 10.8a15.1 15.1 0 0 0 6.6 6.6l2.2-2.2c.3-.3.7-.4 1-.2 1.1.4 2.3.6 3.6.6.6 0 1 .4 1 1V20c0 .6-.4 1-1 1A17 17 0 0 1 3 4c0-.6.4-1 1-1h3.5c.6 0 1 .4 1 1 0 1.3.2 2.5.6 3.6.1.3 0 .7-.2 1z"/></svg>
          +1(555) 418-0293
        </li>
        <li>
          <svg class="contact-icon" viewBox="0 0 24 24"><path d="M2 5h20v14H2zm2 2v.5l8 5 8-5V7l-8 5z"/></svg>
          HELLO@RINGFORGEHUB.COM
        </li>
        <li>
          <svg class="contact-icon" viewBox="0 0 24 24"><path d="M12 2a10 10 0 1 0 0 20 10 10 0 0 0 0-20zm0 2c.9 1.2 1.6 2.6 2 4h-4c.4-1.4 1.1-2.8 2-4zM4.3 14a8 8 0 0 1 0-4h3.4a17 17 0 0 0 0 4zm5.4 0a15 15 0 0 1 0-4h4.6a15 15 0 0 1 0 4zm6.6 0a17 17 0 0 0 0-4h3.4a8 8 0 0 1 0 4zM10 16h4c-.4 1.4-1.1 2.8-2 4-.9-1.2-1.6-2.6-2-4z"/></svg>
          WWW.RINGFORGEHUB.COM
        </li>
        <li>
          <svg class="contact-icon" viewBox="0 0 24 24"><circle cx="12" cy="12" r="10"/></svg>
          g.page/RingForgeHUB?gm
        </li>
        <li>
          <span class="social-pair"><span class="social-square"></span><span class="social-square"></span></span>
          @THEGEMSTONECRAFTSTUDIO
        </li>
      </ul>
      <p class="address">4872 Brambleton Avenue<br>Suite 512 Larkfield, OR</p>
    </div>
  </section>
</main>
</body>
</html>
```